Solar WiFi Charging Bench

Sales Brochure using only the colors of the Tavenish Color Palette provided.
Municipal Government target customer.
Key Features are as follows:
LED Advertising display
Connection to internet (User Defined)
800W Solar
USB-A and USB-C cell phone charging ports
400ah battery backup with low voltage shutoff
Insulated for -40 Deg C
Wireless cell phone charging
Vandalism resistant.
Theft resistant

```html
<!DOCTYPE html>
<html lang="en">
<head>
<meta charset="utf-8">
<title>Solar Charging WiFi Advertising Bench – Tavenish Renewables</title>
<link rel="stylesheet" href="https://fonts.googleapis.com/css2?family=Montserrat:wght@500;600;800&display=swap">
<style>
  :root {
    --brand-blue: #3f55a8;
    --brand-green: #6cc04a;
    --icon-cyan: #3ec4ef;
    --ink-navy: #14254f;
    --night: #060606;
    --white: #ffffff;
    --page: #ffffff;
  }
  html, body {
    margin: 0;
    padding: 0;
    width: 1200px;
    height: 2260px;
    overflow: hidden;
    background: var(--page);
  }
  .brochure {
    position: absolute;
    left: 50px;
    top: 417px;
    width: 1100px;
    height: 1425px;
    box-shadow: 0 6px 24px rgba(0,0,0,0.18);
  }
  .brochure svg { display: block; width: 100%; height: 100%; }
  .headline { font-family: "Montserrat", sans-serif; font-weight: 800; }
  .headline--main { fill: var(--white); font-size: 37px; }
  .headline--sub { fill: var(--brand-green); font-size: 27px; }
  .brand-name { font-family: "Montserrat", sans-serif; font-weight: 800; fill: var(--brand-blue); font-size: 25px; }
  .feature-label { font-family: "Montserrat", sans-serif; font-weight: 500; fill: var(--white); font-size: 15px; }
  .feature-ring { fill: var(--night); stroke: var(--brand-green); stroke-width: 3.5; }
  .feature-disc { fill: var(--icon-cyan); }
  .feature-icon { fill: none; stroke: var(--ink-navy); stroke-width: 3; stroke-linecap: round; stroke-linejoin: round; }
  .connector { fill: none; stroke: var(--brand-green); stroke-width: 2; stroke-dasharray: 2 4; }
  .anchor-dot { fill: var(--brand-blue); }
  .footer-text { font-family: "Montserrat", sans-serif; font-weight: 500; fill: var(--white); font-size: 17px; }
  .footer-call { font-weight: 800; }
  .footer-web { font-family: "Montserrat", sans-serif; font-weight: 600; fill: var(--night); font-size: 21px; }
</style>
</head>
<body>
<div class="brochure">
  <svg viewBox="0 0 795 1030" xmlns="http://www.w3.org/2000/svg">
    <defs>
      <linearGradient id="sceneTones" x1="0" y1="0" x2="0" y2="1">
        <stop offset="0" stop-color="#a9c3dc"/>
        <stop offset="0.35" stop-color="#b9c3c6"/>
        <stop offset="0.55" stop-color="#7c7460"/>
        <stop offset="0.7" stop-color="#3c3426"/>
        <stop offset="0.82" stop-color="#060606"/>
        <stop offset="1" stop-color="#060606"/>
      </linearGradient>
      <linearGradient id="benchTones" x1="0" y1="0" x2="0" y2="1">
        <stop offset="0" stop-color="#b8aea2"/>
        <stop offset="0.5" stop-color="#cfcac4"/>
        <stop offset="0.75" stop-color="#e6e6ea"/>
        <stop offset="1" stop-color="#d9d9de"/>
      </linearGradient>
    </defs>

    <!-- scene backdrop -->
    <rect class="scene-backdrop" x="0" y="0" width="795" height="1030" fill="url(#sceneTones)" role="img" aria-label="Photo backdrop: sky, evergreen trees, grass field and a building"/>

    <!-- header bands -->
    <polygon points="0,0 795,0 795,238 0,42" fill="var(--brand-blue)"/>
    <polygon points="0,42 795,238 795,282 0,56" fill="var(--brand-green)"/>

    <!-- bench product photo -->
    <rect class="bench-photo" x="218" y="130" width="364" height="570" rx="18" fill="url(#benchTones)" role="img" aria-label="Photo of the solar charging bench with its curved solar canopy, wooden seat and LED screen, a woman seated using her phone"/>

    <!-- brand panel -->
    <path d="M50,0 H258 L240,152 Q238,168 222,168 H66 Q50,168 50,152 Z" fill="var(--white)"/>
    <circle cx="146" cy="78" r="22" fill="var(--icon-cyan)"/>
    <text class="brand-name" x="146" y="140" text-anchor="middle">TAVENISH</text>

    <!-- headline -->
    <text class="headline headline--main" x="762" y="58" text-anchor="end">SOLAR CHARGING</text>
    <text class="headline headline--sub" x="757" y="90" text-anchor="end">WIFI ADVERTISING</text>
    <text class="headline headline--sub" x="757" y="116" text-anchor="end">BENCH</text>
    <rect x="704" y="133" width="53" height="3" fill="var(--white)"/>

    <!-- connectors -->
    <path class="connector" d="M160,477 H218"/>
    <path class="connector" d="M643,477 H582"/>
    <path class="connector" d="M160,645 H218"/>
    <path class="connector" d="M643,645 H582"/>
    <path class="connector" d="M145,795 L220,745 V690"/>
    <path class="connector" d="M255,787 V700"/>
    <path class="connector" d="M395,787 V700"/>
    <path class="connector" d="M535,787 V700"/>
    <path class="connector" d="M660,795 L582,740 V690"/>
    <circle class="anchor-dot" cx="218" cy="477" r="4"/>
    <circle class="anchor-dot" cx="582" cy="477" r="4"/>
    <circle class="anchor-dot" cx="218" cy="645" r="4"/>
    <circle class="anchor-dot" cx="582" cy="645" r="4"/>
    <circle class="anchor-dot" cx="222" cy="690" r="4"/>
    <circle class="anchor-dot" cx="255" cy="700" r="4"/>
    <circle class="anchor-dot" cx="395" cy="700" r="4"/>
    <circle class="anchor-dot" cx="535" cy="700" r="4"/>
    <circle class="anchor-dot" cx="578" cy="690" r="4"/>

    <!-- feature: theft resistant -->
    <g class="feature" transform="translate(115,477)">
      <circle class="feature-ring" r="48"/><circle class="feature-disc" r="40"/>
      <rect class="feature-icon" x="-11" y="-4" width="22" height="18" rx="2"/>
      <path class="feature-icon" d="M-7,-4 V-11 A7,7 0 0 1 7,-11 V-4"/>
      <text class="feature-label" y="70" text-anchor="middle">Theft</text>
      <text class="feature-label" y="88" text-anchor="middle">resistant</text>
    </g>
    <!-- feature: vandalism resistant -->
    <g class="feature" transform="translate(688,477)">
      <circle class="feature-ring" r="48"/><circle class="feature-disc" r="40"/>
      <path class="feature-icon" d="M0,-18 L15,-12 V2 Q15,13 0,19 Q-15,13 -15,2 V-12 Z"/>
      <path class="feature-icon" d="M-6,0 L-1,5 L7,-5"/>
      <text class="feature-label" y="70" text-anchor="middle">Vandalism</text>
      <text class="feature-label" y="88" text-anchor="middle">resistant</text>
    </g>
    <!-- feature: battery -->
    <g class="feature" transform="translate(115,645)">
      <circle class="feature-ring" r="48"/><circle class="feature-disc" r="40"/>
      <path class="feature-icon" d="M0,-20 L20,16 H-20 Z"/>
      <path class="feature-icon" d="M2,-8 L-5,4 H4 L-2,12"/>
      <text class="feature-label" y="70" text-anchor="middle">400ah battery</text>
      <text class="feature-label" y="88" text-anchor="middle">backup with low</text>
      <text class="feature-label" y="106" text-anchor="middle">voltage shutoff</text>
    </g>
    <!-- feature: usb ports -->
    <g class="feature" transform="translate(688,645)">
      <circle class="feature-ring" r="48"/><circle class="feature-disc" r="40"/>
      <circle class="feature-icon" cx="3" cy="3" r="15"/>
      <rect class="feature-icon" x="-16" y="-20" width="8" height="12" rx="1"/>
      <path class="feature-icon" d="M-12,-8 V-2"/>
      <text class="feature-label" y="70" text-anchor="middle">USB-A and</text>
      <text class="feature-label" y="88" text-anchor="middle">USB-C cell phone</text>
      <text class="feature-label" y="106" text-anchor="middle">charging ports</text>
    </g>
    <!-- feature: LED display -->
    <g class="feature" transform="translate(115,832)">
      <circle class="feature-ring" r="48"/><circle class="feature-disc" r="40"/>
      <rect class="feature-icon" x="-18" y="-16" width="36" height="32" rx="5"/>
      <text class="feature-label" y="70" text-anchor="middle">LED</text>
      <text class="feature-label" y="88" text-anchor="middle">Advertising</text>
      <text class="feature-label" y="106" text-anchor="middle">display</text>
    </g>
    <!-- feature: internet -->
    <g class="feature" transform="translate(255,832)">
      <circle class="feature-ring" r="48"/><circle class="feature-disc" r="40"/>
      <circle class="feature-icon" r="17"/>
      <ellipse class="feature-icon" rx="7" ry="17"/>
      <path class="feature-icon" d="M-17,0 H17 M-14,-9 H14 M-14,9 H14"/>
      <text class="feature-label" y="70" text-anchor="middle">Connection</text>
      <text class="feature-label" y="88" text-anchor="middle">to internet</text>
      <text class="feature-label" y="106" text-anchor="middle">(User Defined)</text>
    </g>
    <!-- feature: solar -->
    <g class="feature" transform="translate(395,832)">
      <circle class="feature-ring" r="48"/><circle class="feature-disc" r="40"/>
      <path class="feature-icon" d="M-18,-8 H8 L4,18 H-22 Z M-20,5 H6 M-9,-8 L-13,18"/>
      <circle class="feature-icon" cx="14" cy="-14" r="5"/>
      <text class="feature-label" y="70" text-anchor="middle">800W</text>
      <text class="feature-label" y="88" text-anchor="middle">Solar</text>
    </g>
    <!-- feature: wireless charging -->
    <g class="feature" transform="translate(535,832)">
      <circle class="feature-ring" r="48"/><circle class="feature-disc" r="40"/>
      <circle class="feature-icon" r="20"/>
      <rect class="feature-icon" x="-7" y="-13" width="14" height="26" rx="3"/>
      <path class="feature-icon" d="M1,-6 L-3,1 H3 L-1,7"/>
      <text class="feature-label" y="70" text-anchor="middle">Wireless cell</text>
      <text class="feature-label" y="88" text-anchor="middle">phone charging</text>
    </g>
    <!-- feature: insulated -->
    <g class="feature" transform="translate(690,832)">
      <circle class="feature-ring" r="48"/><circle class="feature-disc" r="40"/>
      <path class="feature-icon" d="M-4,4 V-16 A4,4 0 0 1 4,-16 V4"/>
      <circle class="feature-icon" cx="0" cy="9" r="6"/>
      <path class="feature-icon" d="M-18,20 H18 M9,-14 H15 M9,-6 H15"/>
      <text class="feature-label" y="70" text-anchor="middle">Insulated for</text>
      <text class="feature-label" y="88" text-anchor="middle">-40 - +40 Deg C</text>
    </g>

    <!-- footer -->
    <polygon points="0,985 440,985 420,1030 0,1030" fill="var(--brand-blue)"/>
    <polygon points="440,985 795,985 795,1030 420,1030" fill="var(--brand-green)"/>
    <text class="footer-text" x="38" y="1013"><tspan class="footer-call">Call US:</tspan></text>
    <g class="footer-phone" transform="translate(130,1006)">
      <path d="M-4,-6 Q-6,0 0,6 L3,4 L1,1 L-1,2 Q-3,0 -2,-2 L0,-3 L-2,-7 Z" fill="var(--icon-cyan)"/>
    </g>
    <text class="footer-text" x="145" y="1013">780.555.0142</text>
    <g class="footer-phone" transform="translate(277,1006)">
      <path d="M-4,-6 Q-6,0 0,6 L3,4 L1,1 L-1,2 Q-3,0 -2,-2 L0,-3 L-2,-7 Z" fill="var(--icon-cyan)"/>
    </g>
    <text class="footer-text" x="292" y="1013">403.555.0187</text>
    <text class="footer-web" x="438" y="1013">www.tavenishrenewables.com</text>
  </svg>
</div>
</body>
</html>
```